C2C website is looking for a web-designer

Complete description of the project you will find in the file atteched (we updated information there and maybe now it will be easier to understand what it's all about). We are a small team of two people from the Czech Republic and we want to create a united platform in the form of adverts, where people can find smb who will help them to cope with the everyday routine (cooking, cleaning, pet care, house work etc.)
Updates
Project Deadline Extended Reason: We want the designers to have more time for work. Added Wednesday, September 24, 2014
This brief depends on brief 416290 - http://tasks.plumvexa.com/task.aspx?id=416290 (logo design). Both are for the same project. Added Wednesday, September 24, 2014
Industry/Entity Type
House
Number of Pages Required
5+ page
Look and feel
Each slider illustrates characteristics of the customer's brand and the style your logo design should communicate.

```html
<!DOCTYPE html>
<html lang="en">
<head>
<meta charset="utf-8">
<title>HelpiDomov.cz – Advertising Portal</title>
<link rel="stylesheet" href="https://fonts.googleapis.com/css2?family=Lato:wght@300;400;700&display=swap">
<style>
:root{
  --red:#e8676a;
  --red-dark:#d9585b;
  --ink:#333333;
  --text:#555555;
  --muted:#8a8a8a;
  --page:#f3f3f3;
  --panel:#ffffff;
  --line:#e4e4e4;
  --cat:#f0f0f0;
  --dark:#232323;
  --btn-dark:#3d3536;
  --input:#f1f1f1;
}
*{box-sizing:border-box;margin:0;padding:0}
html,body{width:1200px;height:2346px;overflow:hidden}
body{position:relative;background:var(--page);font-family:'Lato',Arial,sans-serif;color:var(--text)}
.abs{position:absolute}
a{color:inherit;text-decoration:none}

/* top bar */
.topbar{left:0;top:0;width:1200px;height:71px;background:var(--panel);border-bottom:1px solid var(--line)}
.brand{left:126px;top:20px;font-size:32px;font-weight:400;color:var(--ink);letter-spacing:-.3px}
.brand-tag{left:393px;top:38px;font-size:12px;color:var(--muted)}
.top-links{top:34px;font-size:12px;color:var(--text)}
.post-btn{left:995px;top:12px;width:81px;height:51px;background:var(--red);color:#fff;font-size:12px;display:flex;align-items:center;justify-content:center}

/* profile row */
.userbar{left:0;top:71px;width:1200px;height:102px;background:var(--panel)}
.avatar{left:143px;top:12px;width:98px;height:79px;border:1px solid var(--red);padding:3px}
.avatar .fill{width:100%;height:100%;background:linear-gradient(160deg,#c9b3a3,#8d7566)}
.user-name{left:261px;top:53px;font-size:13px;color:var(--muted)}
.user-role{left:261px;top:73px;font-size:11px;color:var(--muted)}
.user-links{left:378px;top:15px;font-size:13px;line-height:25.5px;color:var(--muted)}
.field-label{top:34px;font-size:12px;color:var(--text)}
.field{top:31px;height:24px;background:var(--input)}
.login-btn{left:1013px;top:31px;width:53px;height:21px;background:var(--red);color:#fff;font-size:11px;display:flex;align-items:center;justify-content:center}
.forgot{left:632px;top:67px;font-size:9px;color:var(--text)}

/* nav */
.mainnav{left:0;top:173px;width:1200px;height:44px;background:var(--red)}
.mainnav ul{list-style:none;position:absolute;left:137px;top:14px;display:flex;gap:16px;font-size:12.5px;color:#fff}
.mainnav li.current{color:var(--ink)}
.nav-search{left:940px;top:11px;width:136px;height:26px;background:#f4f4f4;display:flex}
.nav-search span{flex:1;font-size:11px;color:#999;padding:6px 8px}
.nav-search i{width:27px;height:26px;background:#bdbdbd;display:flex;align-items:center;justify-content:center}

/* hero */
.hero{left:0;top:217px;width:1200px;height:385px;background:radial-gradient(ellipse at 50% 45%,#6a6a6a 0%,#4a4a4a 55%,#2e2e2e 100%)}
.hero-icon{left:553px;top:20px}
.hero-title{left:0;top:138px;width:1200px;text-align:center;font-size:66px;font-weight:400;color:#fff;letter-spacing:-.5px}
.hero-sub{left:0;top:231px;width:1200px;text-align:center;font-size:18px;color:#fff}
.hero-search{left:213px;top:284px;width:779px;height:34px;background:#fff;border-radius:8px;box-shadow:0 0 0 4px rgba(255,255,255,.35);display:flex;align-items:center;padding:0 22px;font-size:14px;color:#555;justify-content:space-between}

/* recent projects */
.section-title{font-size:20px;color:var(--ink);font-weight:400}
.recent{left:123px;top:668px;width:953px;height:113px;display:flex;justify-content:space-between}
.recent .tile{width:137px;height:113px}

/* sidebar */
.sidebar{left:121px;top:803px;width:306px;height:772px;background:var(--panel);box-shadow:0 0 3px rgba(0,0,0,.08)}
.sidebar h2{position:absolute;left:20px;top:14px;font-size:20px;font-weight:400;color:var(--ink)}
.cat-list{list-style:none;position:absolute;left:3px;top:60px;width:300px}
.cat-list li{height:42.5px;margin-bottom:1px;background:var(--cat);font-size:15px;color:var(--text);display:flex;align-items:center;padding-left:24px}
.cat-list li::before{content:"»";margin-right:18px;font-size:14px}
.cat-list li.active{background:var(--red);color:#fff}

/* main panel */
.main{left:452px;top:803px;width:624px;height:772px;background:var(--panel);box-shadow:0 0 3px rgba(0,0,0,.08)}
.main h2{position:absolute;font-size:21px;font-weight:400;color:var(--ink)}
.main p.body{position:absolute;left:24px;top:55px;width:578px;font-size:11.5px;line-height:20.5px;color:var(--text)}
.main h3{position:absolute;top:155px;font-size:19px;font-weight:400;color:var(--ink)}
.bullets{position:absolute;top:193px;list-style:none;font-size:12px;line-height:20.5px;color:var(--text)}
.bullets li::before{content:"›";margin-right:8px}
.pager{position:absolute;display:flex;gap:10px}
.pager span{width:16px;height:14px;background:#eee;font-size:11px;line-height:13px;text-align:center;color:#666}
.promo{position:absolute;left:24px;top:366px;width:590px;height:115px;display:flex;gap:17px}
.promo div{width:186px;height:115px}
.quote{position:absolute;left:34px;top:573px;width:556px;text-align:center;font-size:12px;line-height:20.5px;color:#9a9a9a}
.t-photo{position:absolute;left:258px;top:644px;width:109px;height:90px;border:1px solid var(--red);padding:3px}
.t-photo div{width:100%;height:100%;background:linear-gradient(160deg,#d2c4b6,#7d6d63)}
.t-name{position:absolute;right:372px;top:697px;font-size:12px;color:var(--red)}
.t-role{position:absolute;right:372px;top:717px;font-size:11px;color:#c0c0c0}

/* featured */
.featured{left:0;top:1591px;width:1200px;height:318px;background:var(--panel)}
.featured h2{position:absolute;left:0;top:10px;width:1200px;text-align:center;font-size:22px;font-weight:400;color:var(--ink)}
.featured .rule{position:absolute;left:534px;top:46px;width:146px;height:2px;background:var(--red)}
.feat-tile{position:absolute;top:81px;width:210px;height:186px}
.arrow{position:absolute;top:161px;width:36px;height:36px;border-radius:50%;background:#e9e9e9;display:flex;align-items:center;justify-content:center}
.more-btn{left:520px;top:1890px;width:159px;height:41px;background:var(--btn-dark);color:#fff;font-size:17px;display:flex;align-items:center;justify-content:center}

/* cta */
.cta{left:123px;top:1969px;width:950px;height:113px;background:var(--red);color:#fff}
.cta h2{position:absolute;left:20px;top:22px;font-size:17px;font-weight:400}
.cta p{position:absolute;left:20px;top:61px;width:750px;font-size:11px;line-height:16px}
.cta-btn{position:absolute;left:787px;top:34px;width:142px;height:49px;border:1px solid #fff;display:flex;align-items:center;justify-content:center;font-size:17px}

/* footer */
.footer{left:0;top:2107px;width:1200px;height:227px;background:var(--dark);color:#fff}
.footer h4{position:absolute;top:24px;font-size:13px;font-weight:400;letter-spacing:.3px}
.footer p{position:absolute;font-size:10.5px;line-height:15px}
.thumb{position:absolute;width:62px;height:61px}
.tweet{position:absolute;left:616px;width:235px;display:flex;gap:8px;font-size:10.5px;line-height:15px}
.tweet i{flex:none;width:20px;height:20px;background:#fff;border-radius:3px;margin-top:2px}
.news-input{position:absolute;left:860px;top:62px;width:211px;height:33px;background:#4a4a4a;font-size:10.5px;padding:10px 11px}
.send{position:absolute;left:1006px;top:107px;width:65px;height:24px;background:var(--red);font-size:11px;display:flex;align-items:center;justify-content:center}
.social{position:absolute;top:148px;width:29px;height:29px;display:flex;align-items:center;justify-content:center}
.social i{width:10px;height:10px;background:#fff}
.stripe{left:0;top:2334px;width:1200px;height:12px;background:var(--red)}
</style>
</head>
<body>

<header class="abs topbar">
  <div class="abs brand">Helpi<span style="color:var(--red)">Domov</span>.cz</div>
  <div class="abs brand-tag" style="left:394px">Advertising Portal</div>
  <div class="abs top-links" style="left:677px">
    <svg width="10" height="10" viewBox="0 0 10 10" style="vertical-align:-1px;margin-right:4px"><path d="M2 0.5l2 2-1 1.5c.7 1.3 1.7 2.3 3 3l1.5-1 2 2-1.5 1.5C4.5 9.5.5 5.5 .5 2z" fill="#777"/></svg>Call us : +420-5550-1234</div>
  <div class="abs top-links" style="left:863px">Get Register</div>
  <div class="abs top-links" style="left:956px">Login</div>
  <a class="abs post-btn">+Postadvert</a>
</header>

<section class="abs userbar">
  <div class="abs avatar"><div class="fill" role="img" aria-label="Portrait photo of the signed-in member"></div></div>
  <div class="abs user-name">Petr Novak</div>
  <div class="abs user-role">Executive</div>
  <div class="abs user-links">My profile<br>Messages<br>Submissions</div>
  <div class="abs field-label" style="left:630px">Username:</div>
  <div class="abs field" style="left:701px;width:105px"></div>
  <div class="abs field-label" style="left:817px">Password :</div>
  <div class="abs field" style="left:890px;width:105px"></div>
  <a class="abs login-btn">Login</a>
  <div class="abs forgot">Register Now | Forgot Password</div>
</section>

<nav class="abs mainnav">
  <ul>
    <li class="current">Home</li><li>About Us</li><li>Categories</li><li>Features</li><li>Discussion</li><li>Articles</li><li>Users</li><li>Registration</li><li>Addadvert</li><li>Contact</li>
  </ul>
  <div class="abs nav-search"><span>Search</span><i><svg width="11" height="11" viewBox="0 0 11 11"><circle cx="4.5" cy="4.5" r="3.3" fill="none" stroke="#fff" stroke-width="1.5"/><path d="M7 7l3 3" stroke="#fff" stroke-width="1.6"/></svg></i></div>
</nav>

<section class="abs hero" role="img" aria-label="Background mosaic of household and everyday objects in grey tones">
  <svg class="abs hero-icon" width="96" height="106" viewBox="0 0 96 106">
    <circle cx="32" cy="10" r="9" fill="#fff"/>
    <path d="M26 24h10v30h26l14 32-8 4-12-26H26z" fill="#fff"/>
    <path d="M20 44a30 30 0 1 0 46 32" fill="none" stroke="#fff" stroke-width="8"/>
  </svg>
  <h1 class="abs hero-title">Advertising Offers and Demand</h1>
  <div class="abs hero-sub">Here you will sell quickly and find things easy!</div>
  <div class="abs hero-search"><span>What are you looking for?</span>
    <svg width="12" height="12" viewBox="0 0 12 12"><circle cx="5" cy="5" r="3.6" fill="none" stroke="var(--red)" stroke-width="1.7"/><path d="M7.6 7.6l3.3 3.3" stroke="var(--red)" stroke-width="1.8"/></svg></div>
</section>

<h2 class="abs section-title" style="left:126px;top:616px">Recent Projects</h2>
<div class="abs recent">
  <div class="tile" role="img" aria-label="Woman with a small dog" style="background:linear-gradient(135deg,#e5c49a,#b07a45)"></div>
  <div class="tile" role="img" aria-label="Gloved hand cleaning a surface" style="background:linear-gradient(135deg,#c7d7e6,#8fb0c9)"></div>
  <div class="tile" role="img" aria-label="Gardening with flowers" style="background:linear-gradient(135deg,#6a5a40,#b8423a)"></div>
  <div class="tile" role="img" aria-label="Consulting services office" style="background:linear-gradient(135deg,#dfe7ee,#5d6f80)"></div>
  <div class="tile" role="img" aria-label="Caregiver with elderly women" style="background:linear-gradient(135deg,#e9d7cf,#a4636a)"></div>
  <div class="tile" role="img" aria-label="Colourful paint strokes" style="background:linear-gradient(135deg,#2f6fc4,#e24a2e 55%,#f2b33a)"></div>
</div>

<aside class="abs sidebar">
  <h2>Categories</h2>
  <ul class="cat-list">
    <li class="active">Cooking</li><li>Housework</li><li>Work in the garden</li><li>Pet care</li><li>Baby sitting</li><li>Tutoring</li><li>Elderly care</li><li>Transportation</li><li>Handyman</li><li>Consulting</li><li>Art</li><li>Body care</li><li>Farming</li><li>Animal products</li><li>Hand-made goods</li><li>Other</li>
  </ul>
</aside>

<main class="abs main">
  <h2 style="left:24px;top:16px">About HelpiDomov</h2>
  <p class="body">Aenean pellentesque dolor dui volutpat tortor, ac congue quam dui sed sem. Nullam eu ligula metus, quis facilisis mauris. Pellentesque habitant morbi tristique senectus et netus et. Cras nibh neque, dapibus in ultricies sit amet, aliquam eget velit. Donec nulla lacus, mattis eu ultricies sed, porttitor non nisl. Vestibulum turpis tellus, convallis sed dapibus vitae, malesuada</p>
  <h3 style="left:24px">Our Benefits</h3>
  <ul class="bullets" style="left:24px"><li>Vestibulum ultricies accu tortor</li><li>Tellus at euismod arcu tortor</li><li>Facilisis sit ameted pellent tortor</li><li>Curabitur volutpat condmetortor</li></ul>
  <h3 style="left:326px">Why Choose Us?</h3>
  <ul class="bullets" style="left:326px"><li>Vestibulum ultricies accu tortor</li><li>Tellus at euismod arcu tortor</li><li>Facilisis sit ameted pellent tortor</li><li>Curabitur volutpat condmetortor</li></ul>

  <h2 style="left:28px;top:314px">Promoted Ads</h2>
  <div class="pager" style="left:562px;top:321px"><span>«</span><span>»</span></div>
  <div class="promo">
    <div role="img" aria-label="Person cleaning a sink" style="background:linear-gradient(135deg,#d8dde2,#3c4a66)"></div>
    <div role="img" aria-label="Chopping vegetables" style="background:linear-gradient(135deg,#cfe3c2,#d2452d)"></div>
    <div role="img" aria-label="Woman with a dog on the floor" style="background:linear-gradient(135deg,#efe7de,#6b8a3a)"></div>
  </div>

  <h2 style="left:28px;top:512px">Testimonials</h2>
  <div class="pager" style="left:562px;top:518px"><span>«</span><span>»</span></div>
  <p class="quote">" Cras nibh neque, dapibus in ultricies sit amet, aliquam eget velit. Donec nulla lacus, mattis eu ultricies sed, porttitor non nisl. Vestibulum turpis tellus, convallis sed. Duis aue irure dolor reprehen derit voluptate velit. Excepteur sint occaecat cupidatat non. "</p>
  <div class="t-name">Tomas Berka</div>
  <div class="t-role">Manager</div>
  <div class="t-photo"><div role="img" aria-label="Portrait photo of the reviewer"></div></div>
</main>

<section class="abs featured">
  <h2>Featured Ads</h2>
  <div class="rule"></div>
  <div class="arrow" style="left:37px"><svg width="10" height="14" viewBox="0 0 10 14"><path d="M8 1L2 7l6 6" fill="none" stroke="#fff" stroke-width="2.5"/></svg></div>
  <div class="arrow" style="left:1124px"><svg width="10" height="14" viewBox="0 0 10 14"><path d="M2 1l6 6-6 6" fill="none" stroke="#fff" stroke-width="2.5"/></svg></div>
  <div class="feat-tile" role="img" aria-label="Pepper, grapes and lemon on a board" style="left:129px;background:linear-gradient(135deg,#b8412c,#8aa04a 55%,#e3c07a)"></div>
  <div class="feat-tile" role="img" aria-label="Tea light candles" style="left:373px;background:linear-gradient(135deg,#3b2416,#b9783f 60%,#f0d9a8)"></div>
  <div class="feat-tile" role="img" aria-label="Basket of flowers" style="left:617px;background:linear-gradient(135deg,#e8d3a2,#6b5a6e 60%,#4a3c3a)"></div>
  <div class="feat-tile" role="img" aria-label="Woman in soft light" style="left:862px;background:linear-gradient(135deg,#4a2f2a,#d9b49a 60%,#f4e6d6)"></div>
</section>
<a class="abs more-btn">View More</a>

<section class="abs cta">
  <h2>Are you ready for the posting your ads on HelpiAds ?</h2>
  <p>This is a text board so make sure you are writing here a usefull content lorem ipsum dolor sit amet. Morbi accumsan ipsum velit nam nec tellus a odio tincidunt auctor a ornare odio sed non mauris vitae erat consequat auctor eu in elit.</p>
  <a class="cta-btn">Get Started</a>
</section>

<footer class="abs footer">
  <h4 style="left:128px">ABOUT</h4>
  <p style="left:128px;top:60px;width:215px">Morbi accumsan ipsum velit. Nam nec tellus a odio tincidunt auctor a ornare odio. Sed non mauris vitae erat consequat auctor eu in elit.</p>
  <p style="left:128px;top:143px;width:215px">Class aptent taciti sociosqu ad litora torquent per conubia nostra, per inceptos himenaeos mauris in erat justo.</p>

  <h4 style="left:373px">FEATURED ADS</h4>
  <div class="thumb" role="img" aria-label="Flower basket" style="left:369px;top:57px;background:linear-gradient(135deg,#e6c27a,#5e4a50)"></div>
  <div class="thumb" role="img" aria-label="Basket handle" style="left:446px;top:57px;background:linear-gradient(135deg,#d9b88a,#4a3630)"></div>
  <div class="thumb" role="img" aria-label="Basket of flowers" style="left:518px;top:57px;background:linear-gradient(135deg,#cfa978,#5a4244)"></div>
  <div class="thumb" role="img" aria-label="Candles" style="left:369px;top:128px;background:linear-gradient(135deg,#3b2416,#c58a4c)"></div>
  <div class="thumb" role="img" aria-label="Fruit on a board" style="left:446px;top:128px;background:linear-gradient(135deg,#b8412c,#9aae58)"></div>
  <div class="thumb" role="img" aria-label="Candles" style="left:518px;top:128px;background:linear-gradient(135deg,#4a2c1c,#d69a5c)"></div>

  <h4 style="left:616px">LATEST TWEETS</h4>
  <div class="tweet" style="top:64px"><i></i><span>Morbi accumsan ipsum velit. Nam nec tellus a odio tincidunt auctor</span></div>
  <div class="tweet" style="top:112px"><i></i><span>Morbi accumsan ipsum velit. Nam nec tellus a odio tincidunt auctor</span></div>
  <div class="tweet" style="top:159px"><i></i><span>Morbi accumsan ipsum velit. Nam nec tellus a odio tincidunt auctor</span></div>

  <h4 style="left:860px">NEWS LATTER</h4>
  <div class="news-input">Enter E-mail Address</div>
  <a class="send">Send</a>
  <a class="social" style="left:860px;background:var(--red)"><i></i></a>
  <a class="social" style="left:894px"><i></i></a>
  <a class="social" style="left:928px"><i></i></a>
  <a class="social" style="left:962px"><i></i></a>
  <a class="social" style="left:996px"><i></i></a>
</footer>
<div class="abs stripe"></div>

</body>
</html>
```